Professional, elegant brochure for funeral home

We have a funeral home. We would like a 2 sided brochure. On one side will be 3 columns for our cremation options and on the other side would be 2-3 columns of our burial options. Would like to print it and also will be putting it on our website at www.Varnelhaven.com

Use as examples

https://www.brimtolgrace.com/pricing-and-resources/online-cremation-package-options

https://pelladinechapel.com/wp-content/uploads/Cremation-with-Ceremony-Plans.pdf

We only need a simple 1page (front and back brochure). Once we have decided on the designer I can provide the final content to be placed on the brochure.

Target Market(s)

We are family owned business so Something soft, inviting, personable and looks professionally done.

Industry/Entity Type

Funeral Home

Requirements
Must have
• Look professional. Easy to read
Nice to have
• Softer Muted comforting colors. No bright colors.

```html
<!DOCTYPE html>
<html lang="en">
<head>
<meta charset="utf-8">
<title>Cremation Plans – Varnel Haven Funeral Home</title>
<link href="https://fonts.googleapis.com/css2?family=DM+Serif+Display&family=Montserrat:wght@500;600&display=swap" rel="stylesheet">
<style>
  :root{
    --page:#ffffff;
    --plum:#4a2540;
    --basic-head:#668f64;
    --basic-body:#6f9d6c;
    --family-head:#c98a52;
    --family-body:#e39f57;
    --memorial-head:#62808f;
    --memorial-body:#7090a1;
    --footer-bg:#e4e3dd;
    --footer-text:#3f3f3f;
    --white:#ffffff;
  }
  *{margin:0;padding:0;box-sizing:border-box}
  html,body{width:929px;height:1200px;overflow:hidden;background:var(--page)}
  .sheet{position:relative;width:929px;height:1200px;background:var(--page)}

  .hero{position:absolute;left:28px;top:28px;width:873px;height:451px;overflow:hidden;
    background:linear-gradient(180deg,#b9b9b7 0%,#c4c5c4 55%,#b5c6d0 78%,#9fb7c4 100%)}
  .hero-bouquet{position:absolute;left:0;top:0;width:430px;height:451px;
    background:radial-gradient(ellipse at 30% 45%,#8e4a86 0%,#b86a86 30%,#d9b45a 52%,rgba(200,200,198,0) 78%)}

  .brand{position:absolute;left:480px;top:128px;width:300px;text-align:center;color:var(--white);
    font-family:"DM Serif Display",serif;white-space:nowrap}
  .brand-line{display:flex;align-items:center;justify-content:center;gap:8px}
  .brand-mark{width:12px;height:12px;border-radius:50%;background:var(--white)}
  .brand-name{font-size:30px;letter-spacing:1px;line-height:1;text-transform:uppercase}
  .brand-sub{font-size:14px;letter-spacing:3px;line-height:1;margin-top:4px;text-transform:uppercase}
  .brand-rule{width:220px;height:1px;background:var(--white);margin:10px auto 6px}
  .brand-tagline{font-size:13px}

  .hero-title{position:absolute;left:432px;top:250px;width:400px;text-align:center;color:var(--plum)}
  .hero-title .main{font-family:"DM Serif Display",serif;font-size:70px;line-height:1}
  .hero-title .sub{font-family:"Montserrat",sans-serif;font-weight:500;font-size:43px;letter-spacing:2px;line-height:1;margin-top:6px}

  .plans{position:absolute;left:28px;top:508px;width:873px;height:614px;display:flex}
  .plan{flex:1;color:var(--white);display:flex;flex-direction:column}
  .plan-head{height:110px;padding:16px 0 0 30px;border-top:6px solid rgba(0,0,0,.12)}
  .plan-name{font-family:"DM Serif Display",serif;font-size:46px;line-height:1}
  .plan-kind{font-family:"Montserrat",sans-serif;font-weight:500;font-size:24px;letter-spacing:1px;line-height:1;margin-top:6px}
  .plan-body{flex:1;padding:30px 20px 0 30px}
  .plan-price{font-family:"DM Serif Display",serif;font-size:56px;line-height:1;margin-bottom:22px}
  .plan-price sup{font-size:22px;vertical-align:top;position:relative;top:6px;margin-right:2px}
  .features{list-style:none;font-family:"Montserrat",sans-serif;font-weight:600;font-size:15px;line-height:24.5px}
  .features li{position:relative;padding-left:16px;margin-bottom:10px}
  .features li::before{content:"";position:absolute;left:2px;top:10px;width:5px;height:5px;border-radius:50%;background:var(--white)}

  .plan--basic .plan-head{background:var(--basic-head)}
  .plan--basic .plan-body{background:var(--basic-body)}
  .plan--family .plan-head{background:var(--family-head)}
  .plan--family .plan-body{background:var(--family-body)}
  .plan--memorial .plan-head{background:var(--memorial-head)}
  .plan--memorial .plan-body{background:var(--memorial-body)}

  .contact{position:absolute;left:28px;top:1122px;width:873px;height:51px;background:var(--footer-bg);
    display:flex;align-items:center;justify-content:center;gap:18px;
    font-family:"Montserrat",sans-serif;font-weight:500;font-size:20px;color:var(--footer-text)}
  .contact .dot{width:7px;height:7px;border-radius:50%;background:var(--footer-text)}
</style>
</head>
<body>
<div class="sheet">
  <div class="hero">
    <div class="hero-bouquet" role="img" aria-label="Photo of a bouquet of purple, pink, yellow and white tulips on a pale wooden table"></div>
    <div class="brand">
      <div class="brand-line"><span class="brand-mark"></span><span class="brand-name">Varnel Haven</span></div>
      <div class="brand-sub">Funeral Home</div>
      <div class="brand-rule"></div>
      <div class="brand-tagline">Cremation · Burial · Pre-Planning</div>
    </div>
    <div class="hero-title">
      <div class="main">Cremation</div>
      <div class="sub">PLANS</div>
    </div>
  </div>

  <div class="plans">
    <section class="plan plan--basic">
      <div class="plan-head"><div class="plan-name">Basic</div><div class="plan-kind">CREMATION</div></div>
      <div class="plan-body">
        <div class="plan-price"><sup>$</sup>1,995</div>
        <ul class="features">
          <li>Professional Services</li><li>Transfer of Deceased</li><li>Care &amp; Preparation</li>
          <li>Funeral Ceremony</li><li>Hearse</li><li>Utility Vehicle</li>
          <li>Cremation performed at<br>our On-Site Crematory</li><li>Online Arrangements</li>
          <li>Digital Photo<br>Identification</li>
        </ul>
      </div>
    </section>
    <section class="plan plan--family">
      <div class="plan-head"><div class="plan-name">Family</div><div class="plan-kind">CREMATION</div></div>
      <div class="plan-body">
        <div class="plan-price"><sup>$</sup>2,995</div>
        <ul class="features">
          <li>Professional Services</li><li>Transfer of Deceased</li><li>Care &amp; Preparation</li>
          <li>Funeral Ceremony</li><li>Hearse</li><li>Utility Vehicle</li>
          <li>Cremation performed at<br>our On-Site Crematory</li><li>Online Arrangements</li>
          <li>Digital Photo<br>Identification</li>
        </ul>
      </div>
    </section>
    <section class="plan plan--memorial">
      <div class="plan-head"><div class="plan-name">Memorial</div><div class="plan-kind">CREMATION</div></div>
      <div class="plan-body">
        <div class="plan-price"><sup>$</sup>4,995</div>
        <ul class="features">
          <li>Professional Services</li><li>Transfer of Deceased</li><li>Care &amp; Preparation</li>
          <li>Funeral Ceremony</li><li>Hearse</li><li>Utility Vehicle</li>
          <li>Cremation performed at<br>our On-Site Crematory</li><li>Online Arrangements</li>
          <li>Digital Photo<br>Identification</li>
        </ul>
      </div>
    </section>
  </div>

  <footer class="contact">
    <span>www.varnelhaven.com</span><span class="dot"></span>
    <span>(555) 014-2290</span><span class="dot"></span>
    <span>Alder Creek and Marlow Falls, NY</span>
  </footer>
</div>
</body>
</html>
```